Hydrographic business needs a business card that reaches hunters and off-road enthusiasts

We need a business card for a new hydrographics company catering to customers such as hunters, off-road ATV riders and custom vehicle enthusiasts. A western theme is preferred but professional. Our service should be thought of as upper end graphic design on firearms, off road vehicles, motorcycles, etc... See www.caldorfx.com for ideas on patterns, colors, etc...

Target Market(s)

Hunters, off road enthusiasts, custom car enthusiasts, motorcycle riders...

Industry/Entity Type

Graphic Design

```html
<!DOCTYPE html>
<html lang="en">
<head>
<meta charset="utf-8">
<title>Caldor Hydro Graphics – Business Card</title>
<link href="https://fonts.googleapis.com/css2?family=Ubuntu:wght@400;500;700&display=swap" rel="stylesheet">
<style>
  :root {
    --brand-red: #a3001d;
    --brand-red-deep: #8e0018;
    --card-white: #f1f0ee;
    --backdrop: #8f8f8f;
    --text-on-red: #ffffff;
  }
  * { margin: 0; padding: 0; box-sizing: border-box; }
  html, body {
    width: 1200px; height: 1000px; overflow: hidden;
    background: var(--backdrop);
    font-family: "Ubuntu", sans-serif;
  }
  .sheet {
    position: relative; width: 1200px; height: 1000px;
    display: flex; flex-direction: column; align-items: center; justify-content: center; gap: 60px;
  }
  .card {
    position: relative; width: 630px; height: 360px; overflow: hidden;
    box-shadow: 0 6px 18px rgba(0,0,0,0.25);
  }
  .card-art { position: absolute; inset: 0; width: 100%; height: 100%; }

  /* Front face */
  .card-front { background: var(--card-white); }
  .wordmark {
    position: absolute; top: 88px; left: 0; right: 0;
    display: flex; align-items: center; justify-content: center; gap: 14px;
  }
  .wordmark-dot {
    width: 26px; height: 26px; border-radius: 50%; background: var(--brand-red);
  }
  .wordmark-name {
    font-weight: 700; font-size: 40px; color: var(--brand-red); letter-spacing: 0.5px;
  }

  /* Back face */
  .card-back { background: var(--brand-red); }
  .contact {
    position: absolute; left: 330px; top: 58px; color: var(--text-on-red);
  }
  .contact-name { font-weight: 700; font-size: 24px; letter-spacing: 0.5px; }
  .contact-role { font-size: 14px; margin-top: 2px; }
  .contact-list { list-style: none; font-size: 18px; line-height: 1.35; font-weight: 500; }
  .contact-list.address { margin-top: 40px; }
  .contact-list.lines { margin-top: 14px; }
  .contact-list .indent { padding-left: 22px; }
</style>
</head>
<body>
<main class="sheet">

  <section class="card card-front" aria-label="Business card front">
    <svg class="card-art" viewBox="0 0 630 360" aria-hidden="true">
      <rect width="630" height="360" fill="var(--brand-red)"/>
      <ellipse cx="340" cy="20" rx="430" ry="300" fill="var(--card-white)"/>
      <ellipse cx="340" cy="20" rx="405" ry="272" fill="none" stroke="var(--brand-red)" stroke-width="16"/>
    </svg>
    <div class="wordmark">
      <span class="wordmark-dot"></span>
      <span class="wordmark-name">Caldor Hydro Graphics</span>
    </div>
  </section>

  <section class="card card-back" aria-label="Business card back">
    <svg class="card-art" viewBox="0 0 630 360" aria-hidden="true">
      <circle cx="40" cy="300" r="270" fill="var(--card-white)"/>
    </svg>
    <div class="contact">
      <h1 class="contact-name">WADE CALDOR</h1>
      <p class="contact-role">Designation</p>
      <ul class="contact-list address">
        <li>a : 212 Mesa Ridge Road</li>
        <li class="indent">Cedar Bend, TX 75090</li>
      </ul>
      <ul class="contact-list lines">
        <li>p : 214-555-0186</li>
        <li>e : wade@caldorfx.com</li>
        <li>w : www.caldorfx.com</li>
      </ul>
    </div>
  </section>

</main>
</body>
</html>
```